Business card design needed

I run a Beautician studio (for 7 years now)
I offer
- Vestolin Body Sugaring
- Velumi Glow
- Nails
- Facials
- Manicure
- Foot Treatment
It might not be necessary to list all those treatments?
Maybe the link to the Website is sufficient?
I leave that up to you ...
(more info on www.BuffsAndBrowsByMarisol.com.au)
Vestolin BodySugaring is our biggest success, It replaces waxing.
I would like to incorporate the logo into the Business Card.
We had many complaints regarding our old Business Cards as the Phone Number was to small.
On the backside, we would like a "your next Appointment" section.
Looking forward to you Design, cheers ... Marisol
Buffs by Brows by Marisol
14 Merindo Cct 3912 Berwick
www.BuffsAndBrowsByMarisol.com.au
03 9418 2276

```html
<!DOCTYPE html>
<html lang="en">
<head>
<meta charset="utf-8">
<title>Vestolin Body Sugaring – Business Card</title>
<link rel="stylesheet" href="https://fonts.googleapis.com/css2?family=Cabin:wght@400;500&display=swap">
<style>
  :root {
    --backdrop: #2e2e2e;
    --teal-light: #138071;
    --teal-dark: #0a5450;
    --lime: #8cc63f;
    --leaf: #1aa150;
    --paper: #ffffff;
    --ink: #1d1d1d;
    --ink-soft: #0b2e2b;
    --phone-ink: #0c2623;
    --white: #ffffff;
  }
  * { box-sizing: border-box; margin: 0; padding: 0; }
  html, body {
    width: 1200px;
    height: 949px;
    overflow: hidden;
    background: var(--backdrop);
    font-family: "Cabin", "Gill Sans", sans-serif;
  }
  .canvas {
    position: relative;
    width: 1200px;
    height: 949px;
  }
  .card {
    position: absolute;
    left: 250px;
    width: 700px;
    height: 400px;
    overflow: hidden;
    box-shadow: 0 10px 30px rgba(0,0,0,.45);
  }
  .card--front {
    top: 56px;
    background: radial-gradient(ellipse at 35% 35%, var(--teal-light) 0%, var(--teal-dark) 100%);
  }
  .card--back {
    top: 493px;
    background: var(--paper);
  }
  .card__band {
    position: absolute;
    left: 0; right: 0; bottom: 0;
    height: 48px;
    background: var(--lime);
  }
  .card__band-tab {
    position: absolute;
    right: 0; top: 0;
    width: 32px;
    height: 100%;
    background: var(--leaf);
  }
  .card__band-text {
    position: absolute;
    right: 52px;
    top: 50%;
    transform: translateY(-50%);
    color: var(--white);
    font-size: 16px;
    white-space: nowrap;
  }
  /* front */
  .brand {
    position: absolute;
    left: 70px;
    top: 150px;
    display: flex;
    align-items: center;
    gap: 12px;
    color: var(--white);
    font-size: 26px;
    font-weight: 400;
    white-space: nowrap;
  }
  .brand__dot {
    width: 14px;
    height: 14px;
    border-radius: 50%;
    background: var(--white);
  }
  .address {
    position: absolute;
    right: 355px;
    top: 228px;
    text-align: right;
    color: var(--ink-soft);
    font-size: 15px;
    font-style: normal;
    line-height: 1.35;
    white-space: nowrap;
  }
  .divider {
    position: absolute;
    left: 360px;
    top: 222px;
    width: 2px;
    height: 52px;
    background: var(--ink-soft);
  }
  .phone {
    position: absolute;
    left: 382px;
    top: 231px;
    display: flex;
    align-items: center;
    gap: 12px;
    color: var(--phone-ink);
    font-size: 26px;
    letter-spacing: 1px;
    white-space: nowrap;
  }
  .phone__icon { width: 32px; height: 32px; }
  /* back */
  .appointment {
    position: absolute;
    left: 52px;
    top: 70px;
    display: flex;
    align-items: center;
    gap: 16px;
    color: var(--ink);
    font-size: 26px;
  }
  .appointment__rule {
    width: 4px;
    height: 46px;
    background: var(--lime);
  }
</style>
</head>
<body>
<main class="canvas">

  <section class="card card--front" aria-label="Business card, front">
    <div class="brand">
      <span class="brand__dot"></span>
      <span class="brand__name">Vestolin Body Sugaring</span>
    </div>

    <address class="address">
      Buffs by Brows by Marisol<br>
      14 Merindo Cct 3912 Berwick
    </address>

    <span class="divider"></span>

    <div class="phone">
      <svg class="phone__icon" viewBox="0 0 32 32" aria-hidden="true">
        <circle cx="16" cy="16" r="14.5" fill="none" stroke="currentColor" stroke-width="2"/>
        <path d="M11.5 8.5c.8-.5 1.7-.3 2.2.5l1.4 2.4c.4.7.2 1.5-.4 2l-1 .8c.8 2 2.2 3.5 4.1 4.5l.9-1c.5-.6 1.4-.7 2-.3l2.4 1.5c.8.5 1 1.5.5 2.2l-.9 1.3c-.8 1.1-2.3 1.5-3.6 1-4.6-1.8-7.8-5-9.5-9.6-.5-1.300-.1-2.8 1-3.6z" fill="currentColor"/>
      </svg>
      <span class="phone__number">03 9418 2276</span>
    </div>

    <div class="card__band">
      <span class="card__band-text">www.BuffsAndBrowsByMarisol.com.au</span>
      <span class="card__band-tab"></span>
    </div>
  </section>

  <section class="card card--back" aria-label="Business card, back">
    <div class="appointment">
      <span class="appointment__rule"></span>
      <span class="appointment__label">Your Next Appointment:</span>
    </div>

    <div class="card__band">
      <span class="card__band-text">hello@buffsandbrows.com.au</span>
      <span class="card__band-tab"></span>
    </div>
  </section>

</main>
</body>
</html>
```